Marta Quinlan Photography needs a unique, creative business card/logo design

I need a design for business cards/logo that is unique and creative in the industry. Simplicity is nice, so not too crowded. Something that will catch my customer's eye and remain in their memory. I am primarily a landscape photographer but will be soon may be branching into boudoir photography as well. I have attached my current card.

Industry/Entity Type

Business

Contact Information for Business Card

Marta Quinlan Photography
Phone: 0439 271 504
Email: MartaQuinlanPhotography@brivomail.net
Website: www.pagerly.net/MartaQuinlanPhotography.Aust

Logo Text

Marta Quinlan Photography

Requirements
Must have
• Contact Details on one side
Should not have
• pixelation

```html
<!DOCTYPE html>
<html lang="en">
<head>
<meta charset="utf-8">
<title>Marta Quinlan Photography – Business Card</title>
<link rel="stylesheet" href="https://fonts.googleapis.com/css2?family=PT+Sans:wght@400;700&family=Raleway:wght@300&display=swap">
<style>
  :root {
    --backdrop: #4a3c30;
    --card: #ffffff;
    --ink: #231f20;
    --ink-soft: #2e2e2e;
    --mist: #dcdcdc;
    --logo-ink: #3a3a3a;
  }
  * { box-sizing: border-box; margin: 0; padding: 0; }
  html, body {
    width: 1200px; height: 750px; overflow: hidden;
    background: var(--backdrop);
  }
  .stage { position: relative; width: 1200px; height: 750px; }
  .card {
    position: absolute; top: 228px;
    width: 462px; height: 263px;
    background: var(--card);
    overflow: hidden;
  }
  .card--contact { left: 135px; }
  .card--brand { left: 616px; }

  .card__disc { position: absolute; top: 0; left: 0; }

  .contact { position: absolute; left: 40px; top: 88px; font-family: "PT Sans", sans-serif; color: var(--ink-soft); }
  .contact__name { font-weight: 700; font-size: 18px; letter-spacing: -0.2px; color: var(--ink); margin-bottom: 10px; }
  .contact__list { list-style: none; }
  .contact__item { display: flex; align-items: center; height: 17.6px; font-size: 13px; }
  .contact__icon { width: 20px; display: flex; justify-content: flex-start; padding-left: 3px; }

  .wordmark {
    position: absolute; left: 166px; width: 270px; top: 103px;
    font-family: "Raleway", sans-serif; font-weight: 300;
    color: var(--logo-ink); text-align: center;
    font-size: 16px; letter-spacing: 0.34em; line-height: 32px;
    text-transform: uppercase;
  }
</style>
</head>
<body>
<main class="stage">
  <section class="card card--contact">
    <svg class="card__disc" width="462" height="263" viewBox="0 0 462 263" aria-hidden="true">
      <circle cx="463" cy="131" r="132" fill="var(--mist)"/>
    </svg>
    <div class="contact">
      <h1 class="contact__name">MARTA QUINLAN</h1>
      <ul class="contact__list">
        <li class="contact__item">
          <span class="contact__icon">
            <svg width="9" height="14" viewBox="0 0 9 14" aria-hidden="true"><rect x="0.8" y="0.8" width="7.4" height="12.4" rx="1.2" fill="none" stroke="var(--ink)" stroke-width="1.6"/><rect x="3" y="10.6" width="3" height="1" fill="var(--ink)"/></svg>
          </span>0439 271 504
        </li>
        <li class="contact__item">
          <span class="contact__icon">
            <svg width="11" height="8" viewBox="0 0 11 8" aria-hidden="true"><rect width="11" height="8" fill="var(--ink)"/><path d="M0.5 0.8 L5.5 4.6 L10.5 0.8" fill="none" stroke="#fff" stroke-width="1"/></svg>
          </span>MartaQuinlanPhotography@brivomail.net
        </li>
        <li class="contact__item">
          <span class="contact__icon">
            <svg width="10" height="10" viewBox="0 0 10 10" aria-hidden="true"><rect width="10" height="10" fill="var(--ink)"/></svg>
          </span>MartaQuinlanPhotography.Aust
        </li>
      </ul>
    </div>
  </section>

  <section class="card card--brand">
    <svg class="card__disc" width="462" height="263" viewBox="0 0 462 263" aria-hidden="true">
      <circle cx="0" cy="131" r="132" fill="var(--ink)"/>
    </svg>
    <div class="wordmark">
      <div>Marta Quinlan</div>
      <div>Photography</div>
    </div>
  </section>
</main>
</body>
</html>
```